Invite Card (Ministers) (business cards used for personal invitation to our church)

I need a business card sized advertisement. The card is a replacement for the attached card only much much cooler. I do not want a image background but more of a vectored, flat look with advertising colors.

I have attached a new image of the couple to replace the old image and a new logo to replace the old logo.

I need a PSD with ALL of the layers un-merged & unlocked

The back of the card should carry the same information as the old card.

Use advertising color and a modern flat look and feel.

Target Market(s)

professional audience

Industry/Entity Type

Non-Profit

Contact Information for Business Card

The card is a replacement for the attached card only much much cooler. I do not want a image background but more of a vectored, flat look with advertising colors.

Font styles to use
Sans Serif

Requirements
Must have
• Must have new logo, new image of couple
Should not have
• graphical background

```html
<!DOCTYPE html>
<html lang="en">
<head>
<meta charset="utf-8">
<title>Grace Light Invite Card</title>
<link rel="stylesheet" href="https://fonts.googleapis.com/css2?family=Cinzel:wght@400;700&display=swap">
<style>
  :root {
    --stage: #141414;
    --card-blue: #33c3f0;
    --card-white: #ffffff;
    --ink-blue: #2cb8ea;
    --ink-white: #ffffff;
    --photo-a: #5b4a55;
    --photo-b: #c9a8d6;
  }
  html, body {
    margin: 0;
    padding: 0;
    width: 1200px;
    height: 900px;
    overflow: hidden;
    background: var(--stage);
  }
  .canvas {
    position: relative;
    width: 1200px;
    height: 900px;
    font-family: "Cinzel", serif;
  }
  .card {
    position: absolute;
    top: 306px;
    height: 271px;
    border-radius: 10px;
    overflow: hidden;
    background: var(--card-blue);
  }
  .card-front { left: 150px; width: 438px; }
  .card-back  { left: 608px; width: 441px; }

  .front-band {
    position: absolute;
    left: 0; right: 0; top: 164px; bottom: 0;
    background: var(--card-white);
  }
  .couple-photo {
    position: absolute;
    left: 0; top: 24px;
    width: 245px; height: 247px;
    background: linear-gradient(100deg, var(--photo-a) 0%, #7a4f73 45%, var(--photo-b) 100%);
  }
  .brand-name {
    position: absolute;
    right: 24px; top: 40px;
    margin: 0;
    color: var(--ink-white);
    font-weight: 700;
    font-size: 34px;
    line-height: 1.05;
    text-align: right;
    letter-spacing: 1px;
  }
  .invite-line {
    position: absolute;
    right: 25px; top: 176px;
    margin: 0;
    color: var(--ink-blue);
    font-size: 25px;
    line-height: 30px;
    text-align: right;
    font-variant: small-caps;
  }

  .back-info {
    position: absolute;
    left: 0; right: 0; top: 80px;
    margin: 0;
    color: var(--ink-white);
    text-align: center;
    font-size: 13px;
    line-height: 22px;
    font-variant: small-caps;
    font-weight: 700;
  }
  .schedule {
    position: absolute;
    left: 102px; width: 238px; top: 165px;
    margin: 0; padding: 0;
    list-style: none;
    color: var(--ink-white);
    font-size: 13px;
    line-height: 23px;
    font-variant: small-caps;
  }
  .schedule li { display: flex; align-items: baseline; }
  .schedule .leader {
    flex: 1;
    border-bottom: 1px dotted var(--ink-white);
    margin: 0 2px;
    transform: translateY(-3px);
  }
</style>
</head>
<body>
<main class="canvas">
  <section class="card card-front">
    <div class="front-band"></div>
    <div class="couple-photo" role="img" aria-label="Photo of the ministering couple, smiling, in a dark suit and a lilac dress"></div>
    <h1 class="brand-name">Grace<br>Light</h1>
    <p class="invite-line">You<br>are<br>Invited</p>
  </section>

  <section class="card card-back">
    <p class="back-info">
      gracelightchapel.org<br>
      2140 Cedar Lane - Plano, Tx 75023<br>
      1-800-555-0192
    </p>
    <ul class="schedule">
      <li><span>Sunday</span><span class="leader"></span><span>9:00 Am</span></li>
      <li><span>Sunday</span><span class="leader"></span><span>11:00 Am</span></li>
      <li><span>Wed. Bible Class</span><span class="leader"></span><span>7:00 Pm</span></li>
    </ul>
  </section>
</main>
</body>
</html>
```